Lorn's Cleaners new delivery postcard

We need to advertise for our new pick up and delivery dry cleaning/laundry service.
Mens Business Shirts $2.00
Pants $4.50
Skirts $5.00
Dry Clean Shirt/Blouse $5.00
Dress $9.00
2 Piece Suits $9.00
Updates
We would like to use a 5x7 size postcard, printed on both sides. We would like to add a discount to the card for 25% off of their first order, with the flyer.
We are a famly run dry cleaners. My name is Paula Brandt and my cell # is 614-372-0481. We are trying to expand our business to include free pick and delivery.
If possible can you use the logo I sent some where on the postcard? The phone # for the store is 614-205-3967.
Reason: Still need to get partners approval.
Industry/Entity Type
Business

```html
<!DOCTYPE html>
<html lang="en">
<head>
<meta charset="utf-8">
<title>Paula Brandt Dry Cleaners – Pickup and Delivery Flyer</title>
<link rel="stylesheet" href="https://fonts.googleapis.com/css2?family=Jost:ital,wght@0,300;0,400;0,500;0,600;1,700&family=Roboto+Condensed:wght@700&display=swap">
<style>
  :root {
    --backdrop: #4a4a4c;
    --paper: #ffffff;
    --navy: #0b4f93;
    --headline: #0a4c94;
    --teal: #0a9bbb;
    --sky: #3ebdf0;
    --grey-text: #6b6b6b;
    --ink: #2a2a2a;
  }
  * { margin: 0; padding: 0; box-sizing: border-box; }
  html, body {
    width: 892px; height: 1200px; overflow: hidden;
    background: var(--backdrop);
  }
  .flyer {
    position: absolute; left: 62px; top: 62px;
    width: 768px; height: 1075px;
    background: var(--paper); overflow: hidden;
    font-family: "Jost", sans-serif;
  }
  .headline {
    position: absolute; top: 50px; left: 0; width: 100%;
    text-align: center; color: var(--headline);
    font-weight: 600; font-size: 39px; line-height: 45px; letter-spacing: 0.3px;
  }
  .shirt-photo {
    position: absolute; top: 160px; left: 0; width: 768px; height: 452px;
    background:
      linear-gradient(160deg, rgba(150,110,95,0.55) 0%, rgba(150,110,95,0) 28%),
      linear-gradient(100deg, #d8dbe6 0%, #c7cde3 14%, #e7a9b3 26%, #f0b4bd 38%, #b9cbe2 52%, #a9c2de 64%, #dfe3ef 76%, #c5d0e6 88%, #efe9e4 100%);
  }
  .service-band {
    position: absolute; top: 610px; left: 0; width: 768px; height: 313px;
    background: var(--navy);
  }
  .accent-strip {
    position: absolute; top: 923px; left: 0; width: 768px; height: 26px;
    background: var(--teal);
  }
  .offer-badge {
    position: absolute; left: 473px; top: 465px;
    width: 256px; height: 256px; border-radius: 50%;
    background: var(--paper); text-align: center;
  }
  .offer-percent {
    display: block; margin-top: 35px;
    font-weight: 400; font-size: 66px; line-height: 62px; color: var(--headline);
  }
  .offer-off {
    display: block; font-weight: 400; font-size: 72px; line-height: 66px; color: var(--teal);
  }
  .offer-terms {
    display: block; margin-top: 6px;
    font-weight: 600; font-size: 21px; line-height: 24px; color: var(--grey-text);
  }
  .family-note {
    position: absolute; left: 46px; top: 655px; width: 260px;
    text-align: center; color: var(--sky);
    font-family: "Roboto Condensed", sans-serif; font-weight: 700;
    font-size: 32px; line-height: 43px;
  }
  .benefits {
    position: absolute; left: 338px; top: 741px; list-style: none;
  }
  .benefits li {
    display: flex; align-items: center; height: 38px;
    color: var(--paper); font-style: italic; font-weight: 700;
    font-size: 24px; letter-spacing: 0.3px;
  }
  .benefits svg { width: 24px; height: 24px; margin-right: 12px; flex: none; }
  .brand-dome {
    position: absolute; left: 45px; top: 816px;
    width: 276px; height: 276px; border-radius: 50%;
    background: var(--paper);
  }
  .brand-name {
    position: absolute; left: 45px; top: 930px; width: 276px;
    text-align: center; color: var(--teal);
    font-weight: 500; font-size: 40px; line-height: 46px; letter-spacing: 2px;
  }
  .call-line {
    position: absolute; left: 0; top: 1024px; width: 100%;
    text-align: center; color: var(--ink);
    font-weight: 300; font-size: 21px;
  }
  .call-line strong { font-weight: 600; }
</style>
</head>
<body>
  <main class="flyer">
    <h1 class="headline">THE HIGHEST QUALITY CARE FOR<br>ALL YOUR VALUED GARMENTS</h1>

    <div class="shirt-photo" role="img" aria-label="Photo of pressed dress shirts in pink, blue and striped fabrics hanging on wooden hangers"></div>

    <div class="service-band"></div>
    <div class="accent-strip"></div>

    <div class="offer-badge">
      <span class="offer-percent">25%</span>
      <span class="offer-off">OFF</span>
      <span class="offer-terms">ON YOUR<br>FIRST ORDER</span>
    </div>

    <p class="family-note">WE ARE A<br>FAMLY RUN DRY<br>CLEANERS</p>

    <ul class="benefits">
      <li><svg viewBox="0 0 24 24" aria-hidden="true"><circle cx="12" cy="12" r="11" fill="#3ebdf0"/><path d="M6.5 12.5l3.6 3.4 7.4-7.6" fill="none" stroke="#fff" stroke-width="2.6" stroke-linecap="round" stroke-linejoin="round"/></svg>QUALITY CARE</li>
      <li><svg viewBox="0 0 24 24" aria-hidden="true"><circle cx="12" cy="12" r="11" fill="#3ebdf0"/><path d="M6.5 12.5l3.6 3.4 7.4-7.6" fill="none" stroke="#fff" stroke-width="2.6" stroke-linecap="round" stroke-linejoin="round"/></svg>SPOTLESS GUARANTEE</li>
      <li><svg viewBox="0 0 24 24" aria-hidden="true"><circle cx="12" cy="12" r="11" fill="#3ebdf0"/><path d="M6.5 12.5l3.6 3.4 7.4-7.6" fill="none" stroke="#fff" stroke-width="2.6" stroke-linecap="round" stroke-linejoin="round"/></svg>PICKUP AND DELIVERY</li>
      <li><svg viewBox="0 0 24 24" aria-hidden="true"><circle cx="12" cy="12" r="11" fill="#3ebdf0"/><path d="M6.5 12.5l3.6 3.4 7.4-7.6" fill="none" stroke="#fff" stroke-width="2.6" stroke-linecap="round" stroke-linejoin="round"/></svg>RELIABLE AND AFFORDABLE</li>
    </ul>

    <div class="brand-dome"></div>
    <p class="brand-name">PAULA<br>BRANDT</p>

    <p class="call-line">CALL NOW TO GET FREE PICK AND DELIVERY: <strong>614-205-3967</strong></p>
  </main>
</body>
</html>
```